complete redesign of prelmorax.com , responsive design

Present website should be used for ideation purpose, designer should submit best design which can explain visitor and excite them to download the app.
. By looking at default view of website, students should get the idea about product.

This website to explain about tablet app and it's features, benefits for students, parents and institutes.

This is tablet/Vexo based product to prepare National ( KMR, ZORWN, PUV, Brennick etc) and International competitive exams (YLD, KUW, QVF, DRUX etc) and visitor should get ideas by just looking at the home page.

Institutes can publish their content on Vornaplex.

Student can optimize time and performance on Vornaplex.

Content is same as present website and please use app screenshot to explain the product. screens should be used wherever relevant, refer attached screens. Website must be responsive and easy in navigation.
This is cloud based system and offering prep test , analysis and dynamic testing as per their study plan.

Education

Education

Coded - Design and coding required

5+ page

6b449b
886aae
b7a5cd
e4daeb
f3f1f8
ffffff

• Great design , responsive, easy to grasp the idea. Allow option to register for free app download.
• Project must have all pages as it is in present website.
• I will leave designer to come up with presentation.
• It should not be layout as it is today. Lot of design being submitted by changing just color and icons. I request to come up with your style and you can use contents from present website.

```html
<!DOCTYPE html>
<html lang="en">
<head>
<meta charset="utf-8">
<title>Prelmorax – Prepare for competitive exams</title>
<link href="https://fonts.googleapis.com/css2?family=Montserrat:wght@400;600;700;800&family=Open+Sans:wght@400;600;700&display=swap" rel="stylesheet">
<style>
:root{
  --accent:#6b449b;
  --accent-2:#886aae;
  --accent-3:#b7a5cd;
  --accent-4:#e4daeb;
  --accent-5:#f3f1f8;
  --ink:#24173a;
  --text:#4f4a59;
  --muted:#8a8494;
  --line:#e4daeb;
  --paper:#ffffff;
  --night:#2a1b40;
}
*{box-sizing:border-box;margin:0;padding:0}
html,body{width:1200px;height:3144px;overflow:hidden}
body{font-family:"Open Sans",Arial,sans-serif;color:var(--text);background:var(--paper);font-size:13px;line-height:1.55}
h1,h2,h3,h4,.btn,.nav a{font-family:"Montserrat",Arial,sans-serif}
.wrap{width:1060px;margin:0 auto;position:relative}
.btn{display:inline-block;font-weight:700;font-size:12px;letter-spacing:.5px;text-transform:uppercase;padding:10px 22px;border-radius:2px;text-decoration:none}
.btn-dark{background:var(--ink);color:#fff}
.btn-accent{background:var(--accent);color:#fff}

/* hero */
.hero{position:relative;height:820px;overflow:hidden}
.hero-photo{position:absolute;inset:0;background:linear-gradient(100deg,#3f2a5e 0%,#6b5a80 38%,#9c8fae 60%,#4a3866 100%)}
.hero-shade{position:absolute;inset:0;background:linear-gradient(180deg,rgba(30,18,48,.45) 0%,rgba(30,18,48,.15) 40%,rgba(30,18,48,.55) 100%)}
.topbar{position:relative;height:32px;background:rgba(36,23,58,.85);color:#e4daeb;font-size:11px}
.topbar .wrap{display:flex;align-items:center;height:32px;gap:28px}
.topbar span{display:flex;align-items:center;gap:6px}
.topbar .signin{margin-left:auto;background:#fff;color:var(--ink);font-weight:700;font-size:10px;padding:4px 12px;border-radius:2px}
.header{position:relative;height:90px}
.header .wrap{display:flex;align-items:center;height:90px}
.brand{display:flex;align-items:center;gap:10px;color:#fff;font-family:"Montserrat",sans-serif;font-weight:800;font-size:20px;letter-spacing:1px}
.brand-dot{width:44px;height:44px;border-radius:50%;background:var(--accent-3)}
.nav{margin-left:auto;display:flex;gap:6px}
.nav a{color:#fff;text-decoration:none;font-size:12px;font-weight:600;padding:8px 18px}
.nav a.active{background:var(--accent)}
.hero-copy{position:relative;text-align:center;color:#fff;margin-top:258px}
.hero-copy h1{font-size:42px;line-height:1.2;font-weight:800;letter-spacing:.5px}
.hero-copy h1 em{font-style:normal;color:var(--accent-3)}
.hero-copy p{font-size:17px;margin-top:12px;color:var(--accent-4)}
.stores{position:relative;text-align:center;margin-top:112px;color:#fff}
.stores h4{font-size:13px;letter-spacing:1px;font-weight:700}
.store-list{display:flex;justify-content:center;gap:32px;margin-top:16px}
.store{width:76px;text-align:center;font-size:10px;font-weight:700;font-family:"Montserrat",sans-serif}
.store svg{display:block;margin:0 auto 4px}
.arrow{position:absolute;top:490px;width:30px;height:30px;border-radius:50%;background:rgba(255,255,255,.85)}
.arrow.left{left:12px}.arrow.right{right:12px}
.arrow svg{display:block;margin:8px auto}

/* section heading */
.sec-title{display:flex;align-items:center;justify-content:center;gap:10px;font-size:28px;font-weight:800;color:var(--ink)}
.sec-title .dot{width:36px;height:36px;border-radius:50%;background:var(--accent)}
.sec-title em{font-style:normal;color:var(--accent)}
.lead{text-align:center;font-size:11px;color:var(--muted);width:900px;margin:14px auto 0;line-height:1.6}

/* platform */
.platform{padding-top:50px;height:540px}
.tabs{display:flex;justify-content:center;margin-top:56px;border-bottom:1px solid var(--line);width:1060px;margin-left:auto;margin-right:auto}
.tabs span{font-family:"Montserrat",sans-serif;font-size:10px;font-weight:700;color:var(--muted);padding:10px 34px}
.tabs span.on{color:var(--accent);border-bottom:2px solid var(--accent)}
.features{display:grid;grid-template-columns:repeat(4,1fr);gap:30px;margin-top:34px;text-align:center}
.feature .ico{width:48px;height:48px;border-radius:50%;margin:0 auto;display:flex;align-items:center;justify-content:center;border:1px solid var(--line);background:var(--accent-5)}
.feature .ico.on{background:var(--accent);border-color:var(--accent)}
.feature h3{font-size:15px;color:var(--ink);margin-top:14px;font-weight:700}
.feature p{font-size:10px;color:var(--muted);margin-top:6px;line-height:1.6}
.view-all{text-align:right;font-size:10px;font-weight:700;color:var(--accent);margin-top:14px;font-family:"Montserrat",sans-serif}

/* access band */
.access{background:var(--accent);height:112px}
.access .wrap{display:flex;align-items:center;height:112px;gap:14px}
.access .dot{width:40px;height:40px;border-radius:50%;background:var(--accent-3)}
.access h2{font-size:26px;color:#fff;font-weight:700}
.access .btn{margin-left:32px;padding:14px 30px;font-size:13px}

/* promo */
.promo{margin-top:40px;height:368px;position:relative;background:var(--night)}
.promo-photo{position:absolute;inset:0;background:radial-gradient(ellipse at 60% 50%,#4e3a6c 0%,#33224d 45%,#1e1330 100%)}
.promo .wrap{height:368px;display:flex;align-items:center}
.promo-copy{position:relative;color:#fff;width:360px;margin-left:30px}
.promo-copy small{font-size:12px;color:var(--accent-3)}
.promo-copy h2{font-size:30px;font-weight:800;margin-top:2px}
.promo-copy h3{font-size:16px;font-weight:600;margin-top:8px;line-height:1.4}
.promo-copy .btn{margin-top:16px;background:var(--accent-2);color:#fff}
.tablet{position:absolute;left:560px;top:54px;width:440px;height:260px;border-radius:18px;background:#120b1d;padding:16px 26px}
.tablet .screen{width:100%;height:100%;border-radius:3px;background:linear-gradient(180deg,var(--accent-5) 0%,var(--accent-4) 100%)}
.play{position:absolute;left:744px;top:148px}

/* everything */
.everything{padding-top:80px;height:760px}
.cards{display:grid;grid-template-columns:repeat(3,1fr);gap:36px;margin-top:60px}
.card .pic{height:216px}
.card h4{font-size:12px;color:var(--accent);font-weight:700;margin-top:14px}
.card ul{list-style:none;margin-top:6px}
.card li{font-size:10px;color:var(--text);line-height:1.75;padding-left:10px;position:relative}
.card li:before{content:"";position:absolute;left:0;top:7px;width:4px;height:4px;background:var(--accent)}
.card .btn{margin-top:22px;padding:6px 16px;font-size:10px}

/* partners */
.partners{height:124px;background:var(--accent-5);border-top:1px solid var(--line);border-bottom:1px solid var(--line);margin-top:16px}
.partners .wrap{display:flex;justify-content:space-between;align-items:center;height:124px}
.partner{width:160px;height:56px;background:#fff;border:1px solid var(--line);display:flex;align-items:center;justify-content:center}
.partner i{display:block;width:110px;height:26px;background:var(--accent-4);border-radius:3px}

/* footer */
.footer{height:268px;padding-top:40px}
.footer .wrap{display:grid;grid-template-columns:250px 220px 200px 1fr;gap:30px}
.footer h4{font-size:12px;color:var(--accent);font-weight:700;text-transform:uppercase;margin-bottom:12px}
.footer li{list-style:none;font-size:10px;color:var(--text);line-height:2;display:flex;align-items:center;gap:8px}
.social-box{height:170px;border:1px solid var(--line)}
.social-box .pic{height:100px;background:linear-gradient(135deg,var(--accent-3),var(--accent-5))}
.social-box p{font-size:10px;color:var(--muted);padding:8px 10px}
.bottom{height:96px;background:var(--night)}
.bottom .wrap{display:flex;align-items:center;height:96px}
.bottom .brand{font-size:16px}
.bottom .brand-dot{width:34px;height:34px}
.bottom small{font-size:9px;color:var(--accent-3);margin-left:238px}
.icons{margin-left:auto;display:flex;gap:6px}
.icons i{display:block;width:22px;height:22px;background:#44305f}
</style>
</head>
<body>

<section class="hero">
  <div class="hero-photo" role="img" aria-label="Student studying at a laptop with books"></div>
  <div class="hero-shade"></div>
  <div class="topbar">
    <div class="wrap">
      <span><svg width="10" height="10" viewBox="0 0 24 24"><path fill="#b7a5cd" d="M6.6 10.8a15 15 0 006.6 6.6l2.2-2.2c.3-.3.7-.4 1-.2 1.1.4 2.3.6 3.6.6.6 0 1 .4 1 1V20c0 .6-.4 1-1 1A17 17 0 013 4c0-.6.4-1 1-1h3.5c.6 0 1 .4 1 1 0 1.3.2 2.5.6 3.6.1.3 0 .7-.2 1z"/></svg>+1 555 014 2290</span>
      <span><svg width="10" height="10" viewBox="0 0 24 24"><path fill="#b7a5cd" d="M2 5h20v14H2zm2 2v.5l8 5 8-5V7z"/></svg>1725 Larkmoor Ave, Suite 12 · info@prelmorax.com</span>
      <span class="signin">SIGN IN</span>
    </div>
  </div>
  <div class="header">
    <div class="wrap">
      <div class="brand"><span class="brand-dot"></span>PRELMORAX</div>
      <nav class="nav">
        <a class="active">HOME</a><a>SOLUTIONS</a><a>INSTITUTES</a><a>FAQ</a>
      </nav>
    </div>
  </div>
  <div class="arrow left"><svg width="10" height="14" viewBox="0 0 10 14"><path d="M8 1L2 7l6 6" stroke="#24173a" stroke-width="2" fill="none"/></svg></div>
  <div class="arrow right"><svg width="10" height="14" viewBox="0 0 10 14"><path d="M2 1l6 6-6 6" stroke="#24173a" stroke-width="2" fill="none"/></svg></div>
  <div class="hero-copy">
    <h1>PREPARE FOR COMPETITIVE EXAM<br>WITH <em>FREE</em> VORNAPLEX TABLET APP</h1>
    <p>Enhance your result, Optimize your performance</p>
  </div>
  <div class="stores">
    <h4>APP AVAILABLE ON</h4>
    <div class="store-list">
      <div class="store"><svg width="64" height="72" viewBox="0 0 64 72"><polygon points="32,2 62,19 62,53 32,70 2,53 2,19" fill="#886aae"/></svg>DROIDAL</div>
      <div class="store"><svg width="64" height="72" viewBox="0 0 64 72"><polygon points="32,2 62,19 62,53 32,70 2,53 2,19" fill="#886aae"/></svg>PANELO</div>
      <div class="store"><svg width="64" height="72" viewBox="0 0 64 72"><polygon points="32,2 62,19 62,53 32,70 2,53 2,19" fill="#886aae"/></svg>POMELY</div>
    </div>
  </div>
</section>

<section class="platform">
  <h2 class="sec-title"><span class="dot"></span>THE BIGGEST <em>PLATFORM</em> EVER</h2>
  <p class="lead">Vornaplex is a tablet based cloud platform that helps students prepare for national and international competitive exams. It offers prep tests, detailed analysis and dynamic testing built around each study plan, so learners can optimize both their time and their performance while institutes publish their own content and parents follow every step of progress.</p>
  <div class="tabs"><span class="on">STUDENTS</span><span>INSTITUTE</span><span>PARENTS</span></div>
  <div class="wrap">
    <div class="features">
      <div class="feature">
        <div class="ico on"><svg width="20" height="20" viewBox="0 0 24 24"><path d="M5 5l14 14M19 5L5 19" stroke="#fff" stroke-width="3"/></svg></div>
        <h3>FREE APP</h3>
        <p>Download the app at no cost and start practising right away with full access to tests for every exam you target.</p>
      </div>
      <div class="feature">
        <div class="ico"><svg width="20" height="20" viewBox="0 0 24 24"><path d="M4 12l5 5L20 6" stroke="#6b449b" stroke-width="3" fill="none"/></svg></div>
        <h3>CUSTOM TEST</h3>
        <p>Build tests around your own study plan, pick chapters and difficulty, and let the app adapt to your progress.</p>
      </div>
      <div class="feature">
        <div class="ico"><svg width="20" height="20" viewBox="0 0 24 24"><circle cx="12" cy="12" r="8" stroke="#6b449b" stroke-width="2.5" fill="none"/><path d="M12 7v5l3 3" stroke="#6b449b" stroke-width="2.5" fill="none"/></svg></div>
        <h3>OFFLINE MODE</h3>
        <p>Keep practising without a connection; your answers sync to the cloud as soon as you are back online.</p>
      </div>
      <div class="feature">
        <div class="ico"><svg width="20" height="20" viewBox="0 0 24 24"><path d="M5 20V12M10 20V6M15 20V10M20 20V4" stroke="#6b449b" stroke-width="3"/></svg></div>
        <h3>ANALYTICS</h3>
        <p>Clear reports show strengths, weak topics and time spent so you know exactly where to focus next.</p>
      </div>
    </div>
    <div class="view-all">VIEW ALL ›</div>
  </div>
</section>

<section class="access">
  <div class="wrap">
    <span class="dot"></span>
    <h2>Get Instant Access to all these Features</h2>
    <a class="btn btn-dark">REGISTER NOW</a>
  </div>
</section>

<section class="promo">
  <div class="promo-photo" role="img" aria-label="Hand holding a tablet in a dim room"></div>
  <div class="wrap">
    <div class="promo-copy">
      <small>Spend some time getting to know us</small>
      <h2>WATCH THE PROMO</h2>
      <h3>Lorem ipsum dolor sit amet, consectetur adipiscing elit, sed do eiusmod tempor</h3>
      <a class="btn">LEARN MORE</a>
    </div>
    <div class="tablet"><div class="screen" role="img" aria-label="App screenshot: test dashboard with score analysis"></div></div>
    <svg class="play" width="72" height="72" viewBox="0 0 72 72"><circle cx="36" cy="36" r="33" fill="rgba(107,68,155,.85)" stroke="#fff" stroke-width="3"/><path d="M29 22l20 14-20 14z" fill="#fff"/></svg>
  </div>
</section>

<section class="everything">
  <h2 class="sec-title"><span class="dot"></span>EVERYTHING YOU <em>NEED</em></h2>
  <p class="lead">Everything students, institutes and parents need lives in one place. Students prepare smarter, institutes reach more learners with their own content, and parents stay informed about results and progress through simple reports shared straight from the app.</p>
  <div class="wrap">
    <div class="cards">
      <div class="card">
        <div class="pic" role="img" aria-label="App screenshot: student practice test on a tablet" style="background:linear-gradient(135deg,#e4daeb,#b7a5cd)"></div>
        <h4>STUDENTS</h4>
        <ul>
          <li>Outstanding platform for exam preparation</li>
          <li>Access all test batches on the tablet</li>
          <li>Fine level analysis of every attempt</li>
          <li>Track progress and optimize your time</li>
          <li>Practise anywhere, even when offline</li>
        </ul>
        <a class="btn btn-accent">READ MORE</a>
      </div>
      <div class="card">
        <div class="pic" role="img" aria-label="App screenshot: institute content publishing panel" style="background:linear-gradient(180deg,#f3f1f8 0%,#b7a5cd 100%)"></div>
        <h4>INSTITUTES</h4>
        <ul>
          <li>Complete ecosystem of testing</li>
          <li>Best technology investment</li>
          <li>Organize and manage all your content</li>
          <li>Publish tests to students instantly</li>
          <li>Full picture of class results</li>
        </ul>
        <a class="btn btn-accent">READ MORE</a>
      </div>
      <div class="card">
        <div class="pic" role="img" aria-label="App screenshot: parent progress report view" style="background:linear-gradient(135deg,#b7a5cd,#886aae)"></div>
        <h4>PARENTS</h4>
        <ul>
          <li>Monitor all your kids in one place</li>
          <li>Access results and score history</li>
          <li>Check the current level of each child</li>
          <li>Get complete insight into progress</li>
          <li>Receive regular updates by email</li>
        </ul>
        <a class="btn btn-accent">READ MORE</a>
      </div>
    </div>
  </div>
</section>

<section class="partners">
  <div class="wrap">
    <div class="partner"><i></i></div>
    <div class="partner"><i></i></div>
    <div class="partner"><i></i></div>
    <div class="partner"><i></i></div>
    <div class="partner"><i></i></div>
  </div>
</section>

<footer class="footer">
  <div class="wrap">
    <div>
      <h4>Contact Us</h4>
      <ul>
        <li><svg width="10" height="10" viewBox="0 0 24 24"><path fill="#6b449b" d="M12 2a7 7 0 00-7 7c0 5 7 13 7 13s7-8 7-13a7 7 0 00-7-7zm0 9.5A2.5 2.5 0 1112 6a2.5 2.5 0 010 5.5z"/></svg>1725 Larkmoor Ave, Suite 12</li>
        <li><svg width="10" height="10" viewBox="0 0 24 24"><path fill="#6b449b" d="M12 2a7 7 0 00-7 7c0 5 7 13 7 13s7-8 7-13a7 7 0 00-7-7z"/></svg>Brightwater, 40213</li>
        <li><svg width="10" height="10" viewBox="0 0 24 24"><path fill="#6b449b" d="M6.6 10.8a15 15 0 006.6 6.6l2.2-2.2c.3-.3.7-.4 1-.2 1.1.4 2.3.6 3.6.6.6 0 1 .4 1 1V20c0 .6-.4 1-1 1A17 17 0 013 4c0-.6.4-1 1-1h3.5c.6 0 1 .4 1 1 0 1.3.2 2.5.6 3.6.1.3 0 .7-.2 1z"/></svg>Office: +1 555 014 2290</li>
        <li><svg width="10" height="10" viewBox="0 0 24 24"><path fill="#6b449b" d="M2 5h20v14H2zm2 2v.5l8 5 8-5V7z"/></svg>info@prelmorax.com</li>
      </ul>
    </div>
    <div>
      <h4>Customer Services</h4>
      <ul><li>› Security &amp; Privacy</li><li>› Payment Options</li><li>› Terms of service</li></ul>
    </div>
    <div>
      <h4>General</h4>
      <ul><li>› Home</li><li>› About Us</li><li>› FAQ</li><li>› Contact</li></ul>
    </div>
    <div class="social-box">
      <div class="pic" role="img" aria-label="Social page cover banner"></div>
      <p>Prelmorax on Circlebook · 1,240 people follow this page</p>
    </div>
  </div>
</footer>

<section class="bottom">
  <div class="wrap">
    <div class="brand"><span class="brand-dot"></span>PRELMORAX</div>
    <small>© All Rights Reserved. Copyright Prelmorax 2024</small>
    <div class="icons"><i></i><i></i><i></i></div>
  </div>
</section>

</body>
</html>
```